Velvet & Bloom Hair Extensions needs a business card

We need a business card designed for an online luxury hair extensions business called Velvet & Bloom, we already have a logo and need an innovative business card (2-sided preferably). The strap line for the brand is 'Luxury Hair At Every Touchpoint!'. The brand is a premium brand selling virgin hair extensions and the target market is the mid-affluent ethnic woman as such the design should reflect this. The brand logo is grey and can be sent when requested.

Target Market(s)

25 to 35 year mid-affluent ethnic woman (Afro-American, Mixed Race, Asian)

Industry/Entity Type

Hair

Colors

Designer to choose colors to be used in the design.

Requirements
Must have
• Business Name: Velvet and Bloom
Strapline: Luxury hair at every touchpoint!
Domain: ​www.velvetandbloom-demo.com
Email: info@velvetandbloom-demo.com
sales and enquiries
44 07391 xxxxxxx

Please use the grey main brand logo depicted in page 2 of the attached pdf document

```html
<!DOCTYPE html>
<html lang="en">
<head>
<meta charset="utf-8">
<title>Velvet &amp; Bloom Hair Extensions – Business Card</title>
<link rel="stylesheet" href="https://fonts.googleapis.com/css2?family=Questrial&display=swap">
<style>
  :root {
    --stage: #e9e7e4;
    --ink: #0d0d0d;
    --band: #a3a3a3;
    --paper: #ffffff;
    --soft: #8f8f8f;
    --hair-light: #dcdcdc;
    --hair-dark: #a5a5a5;
  }
  * { box-sizing: border-box; margin: 0; padding: 0; }
  html, body {
    width: 1200px;
    height: 784px;
    overflow: hidden;
    background: var(--stage);
    font-family: "Questrial", "Helvetica Neue", Arial, sans-serif;
  }
  .stage {
    width: 1200px;
    height: 784px;
    display: flex;
    align-items: center;
    justify-content: center;
    gap: 40px;
  }
  .card {
    position: relative;
    width: 540px;
    height: 310px;
    background: var(--ink);
    overflow: hidden;
    box-shadow: 0 10px 28px rgba(0,0,0,0.18);
  }
  .card__shape {
    position: absolute;
    inset: 0;
    width: 100%;
    height: 100%;
  }
  .shape-band { fill: var(--band); }
  .shape-paper { fill: var(--paper); }

  /* Front */
  .hair-art {
    position: absolute;
    right: 44px;
    top: 26px;
    width: 230px;
    height: 170px;
    border-radius: 45% 55% 40% 60% / 50% 45% 55% 50%;
    background: linear-gradient(120deg, var(--hair-dark) 0%, var(--hair-light) 80%);
  }
  .wordmark {
    position: absolute;
    left: 64px;
    top: 212px;
    display: flex;
    align-items: center;
    gap: 10px;
    color: var(--soft);
    font-size: 28px;
    line-height: 1;
    letter-spacing: 0.08em;
    text-transform: uppercase;
    white-space: nowrap;
  }
  .wordmark__dot {
    width: 12px;
    height: 12px;
    border-radius: 50%;
    background: var(--soft);
  }

  /* Back */
  .details {
    position: absolute;
    left: 70px;
    top: 40px;
    right: 60px;
  }
  .strapline {
    color: #b5b5b5;
    font-size: 21px;
    line-height: 1.15;
    letter-spacing: 0.04em;
    text-transform: uppercase;
    text-align: right;
    padding-right: 10px;
  }
  .website {
    margin-top: 22px;
    color: var(--ink);
    font-size: 25px;
  }
  .contact {
    margin-top: 18px;
    color: var(--soft);
    font-size: 18px;
    line-height: 1.35;
  }
</style>
</head>
<body>
<main class="stage">
  <section class="card card--front" aria-label="Business card front">
    <svg class="card__shape" viewBox="0 0 540 310" preserveAspectRatio="none" aria-hidden="true">
      <path class="shape-band" d="M20,0 H540 V262 C500,285 470,310 420,310 H0 V72 C10,44 14,18 20,0 Z"/>
      <path class="shape-paper" d="M46,0 H540 V238 C492,264 462,284 398,284 C330,284 260,310 240,310 H30 V90 C40,58 42,26 46,0 Z"/>
    </svg>
    <div class="hair-art" role="img" aria-label="Grey illustration of a woman's profile with long flowing hair"></div>
    <div class="wordmark">
      <span class="wordmark__dot"></span>
      <span class="wordmark__name">Velvet &amp; Bloom</span>
    </div>
  </section>

  <section class="card card--back" aria-label="Business card back">
    <svg class="card__shape" viewBox="0 0 540 310" preserveAspectRatio="none" aria-hidden="true">
      <path class="shape-band" d="M0,0 H500 C520,28 540,40 540,60 V310 H120 C80,300 40,290 0,250 Z"/>
      <path class="shape-paper" d="M0,0 H470 C500,30 520,50 520,80 V310 H150 C100,300 50,290 22,262 C16,200 8,120 0,40 Z"/>
    </svg>
    <div class="details">
      <p class="strapline">Luxury hair at every<br>touchpoint!</p>
      <p class="website">www.velvetandbloom-demo.com</p>
      <div class="contact">
        <p>sales and enquiries</p>
        <p>44 07391 xxxxxxx</p>
        <p>info@velvetandbloom-demo.com</p>
      </div>
    </div>
  </section>
</main>
</body>
</html>
```